Fresh Produce Outlet needs a Poster Design

Hi,
We are Brightleaf Harvest Market, a fruit and veg outlet based in the suburb of Yanchep, Perth, Western Australia.Apart from fresh produce, we also stock nuts and grains, organic products and specialty grocery. We are about to launch a re-branding exercise, projecting ourselves as 'the' shop for fresh produce; quality, taste and freshness being our key differentiators. We are competing against a big supermarket chain who are using marketing muscle power to shut us down and we want to respond with a series of posters which are simple yet bold and sends a clear and positive message to our customers about what we have to offer.
Please feel free to visit our Facebook page www.facebook.com/brightleafharvestmkt to get an idea about our current branding,logo and the shop in general.
Regards
Team - Brightleaf Harvest Market
Target Market(s)
Residents of Yanchep and surrounding suburbs
Industry/Entity Type
Retail
Look and feel

```html
<!DOCTYPE html>
<html lang="en">
<head>
<meta charset="utf-8">
<title>Brightleaf Harvest Market – Poster</title>
<link rel="stylesheet" href="https://fonts.googleapis.com/css2?family=Nunito:wght@800;900&display=swap">
<style>
  :root {
    --linen: #f1ece2;
    --linen-deep: #e6dfd1;
    --brand-green: #1b9a4a;
    --brand-shadow: rgba(40, 60, 40, 0.35);
    --leaf-light: #8cc63f;
    --veg-green: #5aa83a;
    --veg-dark: #2f7d32;
    --veg-red: #d9342b;
    --veg-yellow: #f2c230;
    --veg-purple: #6a2a6e;
  }
  * { margin: 0; padding: 0; box-sizing: border-box; }
  html, body {
    width: 848px;
    height: 1200px;
    overflow: hidden;
    background: var(--linen);
  }
  .poster {
    position: relative;
    width: 848px;
    height: 1200px;
    overflow: hidden;
    background: radial-gradient(ellipse at 50% 45%, var(--linen) 55%, var(--linen-deep) 100%);
    font-family: "Nunito", "Arial Rounded MT Bold", sans-serif;
  }
  .produce-top-left,
  .produce-top-right {
    position: absolute;
    top: 0;
  }
  .produce-top-left {
    left: 0;
    width: 440px;
    height: 130px;
    border-radius: 0 0 60% 40% / 0 0 100% 80%;
    background: linear-gradient(90deg, #a57a4a 0%, var(--leaf-light) 35%, var(--veg-red) 62%, #b8d98a 100%);
    opacity: 0.85;
  }
  .produce-top-right {
    right: 0;
    width: 340px;
    height: 110px;
    border-radius: 0 0 30% 70% / 0 0 80% 100%;
    background: linear-gradient(90deg, #b7c95a 0%, #f4f0e6 45%, #e9e4d6 70%, var(--leaf-light) 100%);
    opacity: 0.9;
  }
  .brand {
    position: absolute;
    left: 130px;
    top: 200px;
    display: flex;
    align-items: center;
    gap: 28px;
  }
  .brand-mark {
    width: 120px;
    height: 120px;
    border-radius: 50%;
    background: var(--leaf-light);
    flex: none;
  }
  .brand-name {
    font-weight: 800;
    font-size: 56px;
    line-height: 1.05;
    color: var(--brand-green);
  }
  .tagline {
    position: absolute;
    left: 0;
    right: 0;
    top: 390px;
    text-align: center;
    color: var(--brand-green);
    font-weight: 900;
    font-size: 62px;
    line-height: 85px;
    text-shadow: 2px 3px 0 var(--brand-shadow);
  }
  .tagline .line { display: block; }
  .tagline .caps { letter-spacing: 0.5px; }
  .produce-bottom {
    position: absolute;
    left: 0;
    bottom: 0;
    width: 848px;
    height: 560px;
  }
</style>
</head>
<body>
  <main class="poster">
    <div class="produce-top-left" role="img" aria-label="Illustrated potato, lettuce and tomato along the top edge"></div>
    <div class="produce-top-right" role="img" aria-label="Illustrated olive and cauliflower along the top edge"></div>

    <header class="brand">
      <span class="brand-mark" aria-hidden="true"></span>
      <h1 class="brand-name">Brightleaf Harvest<br>Market</h1>
    </header>

    <p class="tagline">
      <span class="line">THE Shop for</span>
      <span class="line">Fresh Produce</span>
      <span class="line caps">QUALITY</span>
      <span class="line caps">TASTE</span>
      <span class="line">and</span>
      <span class="line caps">FRESHNESS</span>
    </p>

    <svg class="produce-bottom" viewBox="0 0 848 560" role="img" aria-label="Illustrated heap of fresh vegetables: peppers, corn, lettuce, tomato, eggplant, mushroom, peas and herbs">
      <defs>
        <linearGradient id="veg-heap" x1="0" y1="0" x2="1" y2="1">
          <stop offset="0" stop-color="#d9342b"/>
          <stop offset="0.25" stop-color="#8cc63f"/>
          <stop offset="0.5" stop-color="#6a2a6e"/>
          <stop offset="0.68" stop-color="#f2c230"/>
          <stop offset="0.85" stop-color="#5aa83a"/>
          <stop offset="1" stop-color="#2f7d32"/>
        </linearGradient>
      </defs>
      <path d="M0 150 C60 120 150 130 200 190 C230 230 250 280 300 300
               C360 320 420 300 470 320 C520 340 560 300 600 260
               C640 210 700 140 760 110 C800 90 830 80 848 70
               L848 560 L0 560 Z" fill="url(#veg-heap)" opacity="0.9"/>
    </svg>
  </main>
</body>
</html>
```